Business Card and Word .doc header and footer required

I need a business card designed for my cybersecurity consulting company. Also required, is a header and footer to be ued for my word documents.
Attached is the Logo design, font and rgb used.

Industry/Entity Type

Cyber Security Consulting

Contact Information for Business Card

Name, Phone, email, website

Colors
0054AA
0677BA
7BADD7
CADEEF
E8F1F8

Requirements
Must have
• Sleek, modern

```html
<!DOCTYPE html>
<html lang="en">
<head>
<meta charset="utf-8">
<title>Harlow Ridge Consulting – Letterhead</title>
<link rel="stylesheet" href="https://fonts.googleapis.com/css2?family=Montserrat:wght@400;600&display=swap">
<style>
  :root {
    --ink: #0b1120;
    --blue-deep: #0677ba;
    --blue-mid: #4a98c4;
    --blue-soft: #7badd7;
    --blue-pale: #a9c3df;
    --paper: #ffffff;
  }
  * { margin: 0; padding: 0; box-sizing: border-box; }
  html, body {
    width: 924px;
    height: 1200px;
    overflow: hidden;
    background: var(--paper);
    font-family: "Montserrat", sans-serif;
  }
  .letterhead {
    position: relative;
    width: 924px;
    height: 1200px;
    background: var(--paper);
  }
  .brand {
    position: absolute;
    left: 40px;
    top: 40px;
    width: 255px;
    display: flex;
    flex-direction: column;
    align-items: center;
  }
  .brand-dot {
    width: 62px;
    height: 62px;
    border-radius: 50%;
    background: var(--blue-deep);
    margin-bottom: 22px;
  }
  .brand-name {
    color: var(--ink);
    font-weight: 600;
    font-size: 22px;
    line-height: 1.15;
    text-align: center;
    letter-spacing: 0.02em;
  }
  .header-rule, .footer-bands {
    position: absolute;
    left: 0;
    display: block;
  }
  .header-rule { top: 160px; }
  .footer-bands { top: 1120px; }
  .contact-line {
    position: absolute;
    top: 1124px;
    left: 230px;
    display: flex;
    gap: 12px;
    font-size: 13.5px;
    color: var(--ink);
  }
  .contact-item { display: flex; align-items: center; gap: 5px; }
  .contact-item svg { width: 12px; height: 12px; }
  .website {
    position: absolute;
    top: 1157px;
    left: 396px;
    color: #ffffff;
    font-size: 14px;
    letter-spacing: 0.42em;
  }
</style>
</head>
<body>
<main class="letterhead">

  <header class="brand">
    <div class="brand-dot"></div>
    <p class="brand-name">HARLOW RIDGE<br>CONSULTING</p>
  </header>

  <svg class="header-rule" width="924" height="44" viewBox="0 0 924 44" aria-hidden="true">
    <defs>
      <linearGradient id="headBand" x1="0" x2="1" y1="0" y2="0">
        <stop offset="0" stop-color="#a9c3df"/>
        <stop offset="1" stop-color="#0677ba"/>
      </linearGradient>
    </defs>
    <polygon points="40,36 382,36 377,40 40,40" fill="#0b1120"/>
    <polygon points="403,3 417,3 401,40 387,40" fill="#a9c3df"/>
    <polygon points="426,3 440,3 424,40 410,40" fill="#9dbbd9"/>
    <polygon points="449,3 463,3 447,40 433,40" fill="#91b3d4"/>
    <polygon points="475,3 924,3 924,40 455,40" fill="url(#headBand)"/>
  </svg>

  <div class="contact-line">
    <span class="contact-item">
      <svg viewBox="0 0 12 12" aria-hidden="true"><circle cx="6" cy="6" r="6" fill="#0677ba"/><path d="M4 3.2l1 1.2-.6.8c.4.8 1 1.4 1.8 1.8l.8-.6 1.2 1-.5 1c-2.4-.2-4.2-2-4.4-4.4z" fill="#fff"/></svg>
      (555) 214-0187
    </span>
    <span class="contact-item">
      <svg viewBox="0 0 12 12" aria-hidden="true"><circle cx="6" cy="6" r="6" fill="#0677ba"/><rect x="3" y="4" width="6" height="4.2" fill="#fff"/><path d="M3 4l3 2.3L9 4" stroke="#0677ba" stroke-width=".8" fill="none"/></svg>
      mara@harlowridge.com
    </span>
  </div>

  <svg class="footer-bands" width="924" height="70" viewBox="0 0 924 70" aria-hidden="true">
    <defs>
      <linearGradient id="footBand" x1="0" x2="1" y1="0" y2="0">
        <stop offset="0" stop-color="#0677ba"/>
        <stop offset="0.62" stop-color="#0677ba"/>
        <stop offset="1" stop-color="#7badd7"/>
      </linearGradient>
    </defs>
    <polygon points="593,7 924,7 924,30 571,30" fill="#0b1120"/>
    <polygon points="265,30 924,30 924,69 228,69" fill="url(#footBand)"/>
  </svg>
  <p class="website">www.harlowridge.com</p>

</main>
</body>
</html>
```